“Be Part Of History! Great Web Design Needed For Local Business!”

Note: This is for design only. No coding required. We want to see your ideas for a great website! This will be a FUN design and not boring like others you may work on.

WE HAVE HAD ONLY 8 DESIGNERS SO FAR SUBMIT - THIS IS A WIDE OPEN CONTEST THAT COULD MAKE YOU GOOD MONEY. PLEASE CONSIDER JOINING!

Look we are needing a great website design for a local carpet cleaning business….I know you are asking how can you “be part of history” with a boring industry like carpet cleaning. Here is the deal….NO ONE in our city has a great design so when you are chosen as the designer you are literally making history by bringing a great design to our city in this industry…

I know it’s cheesy but I am trying to get you to use your skills to help us and make it fun at the same time.

Why work with us:

We are a professional company that has run hundreds of crowdsourced projects on multiple platforms. If you participate in this contest (we hope you do) you can expect great video feedback, consistent feedback, and also our guarantee that if we know your website design will not be what we are looking for we will notify you so you don’t waste your time if there is no chance of you winning.

We respect and recognize this is how you make your living and we will not play games. We look forward to an awesome contest and awesome website designs.

Design Brief:

For this project please let your creative ideas flow. We have given you a ton of info along with videos to help you understand what we are after, however we WANT your creativity to shine through in your designs!

We are looking for a fresh and fun new design for

http://www.brightloomcarpets.example/

This is a local carpet cleaning company that does great work. Unfortunately the current web design is old, outdates, and looks like dirt. So how can they portray a great image with the site they currently have? They can’t so that is why we need your help.

This website needs to convey trust, professionalism, and be super clean and easy to navigate. People making decisions for carpet cleaners are doing this fast so we need to make the site stand out and easy to navigate.

As you can see the current site does not convey trust, looks amateur and does not make people believe that this business has been in business 20 years…this is actually the top company in Albuquerque, but the current site does not reflect that…

Here is a video to help explain what we like about the current site and what we don’t like:

http://clipvista.example/t/qWm4Lp8R

Here are some examples of other sites in their business that have some things we like:

http://www.freshwavecarpet.example/ Please watch video to learn what we like and don’t like:
http://clipvista.example/t/Hx7nTrBBqLp

http://www.tidyharborhomes.example/ Please watch video to learn what we like and don’t like:
http://clipvista.example/t/vRk3QwLs

http://lorenvask.example/ Please watch video to learn what we like and don’t like:
http://clipvista.example/t/JumwdaYe

http://bluemesarugcare.example/ Please watch video to learn what we like and don’t like:
http://clipvista.example/t/TZPR8VbnX

NOTE: We do not want to copy anything outright. We want to learn, model and take their ideas and make them better. We also want to be flexible and take what we like along with your creativity to make an amazing design.

Here is what we are looking for in more specific terms:

Colors: We need to keep the teal/turquoise look of the site. But we need some contrasting colors. Also the client likes white “its clean” so we can use white space in this.

When looking at colors please know that the current site and look is NOT what we are going for. We are going for a clean and professional look but also a look that is BOLD, FUN, and Vibrant (hence the colors).

Menu: Horizontal. We like bold and easy to read menu items. Don’t make it small and cluttered.

Site Structure: Clean and easy to navigate. We have a lot of content to display so we need a clean structure that breaks up the text and content areas.

Images: Please pull images from the current site. We can always replace the images of course, but if you show them “their own stuff” in the new design you will be closer to winning because it will feel more like “them”

Look and Feel: Professional company, trusted, and makes people feel comfortable once they are there. We need to also convey clean and crisp. That is what people are looking for from them.

Content Areas: It is a safe bet that if it is on the current site we need it on the new site. So don’t drop anything as it makes it hard to “cut content”.

What we don't want: We do not want clutter, boring, or templates or themes. We don’t want too cartoony, too cute, or too fancy… Be creative!

WIREFRAME: http://clipvista.example/t/WsDhkoYz

Out of respect to professional designers who really are working hard to win if you do not follow this brief, you submit worn out themes, templates, or boring designs you will be eliminated. We are offering great prize money for this so we expect great visual designs.

We look forward to seeing your great work! Please ask any question if you have them. We will be very responsive throughout this whole contest!

Hi all, I appreciate each of you for taking the time to submit designs. I have spend a considerable amount of time today creating feedback for each of you in written and video format. We are serious about this project and are looking forward to seeing new designs. Thank you! Dale

Hi all, First I want to thank all the designers. We have many good designs and at this point are working with our client to give feedback to all of you. If we gave you feedback them please complete our requests to be considered. If you submitted a design and have not received feedback it means your design is really good, and we are sharing with our clients to get feedback so we don't waste your time on unnecessary changes. Thanks for your patience and we will get back to you soon. Dale

Reason: Hi guys, Client was on vacation and is taking a bit more time to get us feedback. Thanks, Dale

Reason: Extending to allow designers to accommodate changes for us. Dale

Target Market(s)

Most of our clients are higher end affluent. On the residential side we mostly have females calling to book appointments for our service.

We also have large businesses like apartment complexes, office buildings etc calling for our services as well.

Industry/Entity Type

Business

Font styles to use
Sans Serif

Requirements
Must have
• Space for video
Horizontal Menu
Bold
Crisp and Clean
Nice to have
• Coupons, testimonials, services,
Should not have
• cluttered
vertical menu
template look

```html
<!DOCTYPE html>
<html lang="en">
<head>
<meta charset="utf-8">
<title>Brightloom Clean – Carpet &amp; Upholstery Cleaning</title>
<link href="https://fonts.googleapis.com/css2?family=Mulish:wght@400;600;700;800&family=Open+Sans:wght@400;600&family=Oswald:wght@400;500&display=swap" rel="stylesheet">
<style>
:root{
  --teal:#1a9bb7;
  --teal-dark:#137f97;
  --teal-text:#1687a3;
  --green-text:#1f6b3a;
  --ink:#333;
  --muted:#666;
  --line:#e3e3e3;
  --panel:#f6f6f6;
  --footer:#1b1b1b;
  --footer-text:#c9c9c9;
  --star:#e8b21a;
}
*{margin:0;padding:0;box-sizing:border-box}
html,body{width:733px;height:1200px;overflow:hidden}
body{position:relative;background:#fff;font-family:"Open Sans",sans-serif;color:var(--ink)}
.abs{position:absolute}
.carpet-band{left:0;top:0;width:733px;height:355px;background:radial-gradient(circle at 30% 20%,#3a9a5a,#2a7c45 70%)}
.page{left:60px;top:34px;width:613px;height:976px;background:#fff}
.brand{left:76px;top:54px;display:flex;align-items:center;gap:7px}
.brand-mark{width:12px;height:12px;border-radius:50%;background:var(--teal)}
.brand-name{font-family:"Mulish",sans-serif;font-weight:800;font-size:17px;color:var(--teal)}
.phone-icon{left:544px;top:60px}
.phone{left:571px;top:57px;border-left:1px solid var(--line);padding-left:10px;font-family:"Mulish",sans-serif}
.phone b{display:block;font-weight:600;font-size:10px;color:var(--green-text);white-space:nowrap}
.phone span{display:block;font-size:9px;color:var(--muted);margin-top:6px}
.nav{left:76px;top:111px;width:581px;height:33px;background:linear-gradient(#22a8c3,#168fa9);display:flex}
.nav a{font-family:"Mulish",sans-serif;font-weight:600;font-size:7.6px;color:#fff;text-decoration:none;line-height:33px;padding:0 12px;border-right:1px solid rgba(255,255,255,.18)}
.nav a:last-child{border-right:0}
.hero{left:76px;top:154px;width:581px;height:297px;
  background:
    linear-gradient(180deg,rgba(255,255,255,0) 60%,rgba(196,184,168,.85) 82%,#b8aa97 100%),
    linear-gradient(90deg,#cfd2d5 0%,#6f8fb3 22%,#5a7ca6 34%,#e8d7c4 46%,#eee7de 58%,#f4f2ee 78%,#ece9e4 100%)}
.hero-caption{left:476px;top:288px;font-family:"Oswald",sans-serif;font-weight:500;font-size:25px;color:var(--teal-dark);letter-spacing:-.3px}
.hero-arrow{top:413px;width:20px;height:20px;border-radius:50%;background:#444;display:flex;align-items:center;justify-content:center}
.tile{top:466px;width:139px;height:120px;border:1px solid var(--line);background:#fff}
.tile-img{height:92px}
.tile-label{height:27px;display:flex;align-items:center;justify-content:center;gap:20px;font-family:"Mulish",sans-serif;font-size:9px;color:var(--green-text)}
.tile-label.active{background:var(--teal);color:#fff}
.stars{color:var(--star);font-size:7px;letter-spacing:.5px}
.stars i{color:#ccc;font-style:normal}
.divider{left:76px;top:603px;width:581px;height:4px;background:repeating-linear-gradient(90deg,#e6e6e6 0 2px,#f3f3f3 2px 4px)}
.welcome-title{left:76px;top:619px;font-family:"Mulish",sans-serif;font-weight:400;font-size:16.5px;color:#222}
.body-copy{left:76px;width:406px;font-size:6.5px;line-height:12.7px;color:#555}
.sidebar-head{left:501px;top:623px;width:156px;height:27px;background:var(--teal);color:#fff;font-family:"Mulish",sans-serif;font-weight:600;font-size:8.5px;line-height:27px;padding-left:11px}
.niche-list{left:501px;top:650px;width:156px;height:117px;background:#fafafa;border:1px solid #eee;border-top:0;list-style:none;padding:13px 0 0 12px}
.niche-list li{font-size:7.2px;color:#555;height:19px}
.niche-list li::before{content:"›";color:#888;margin-right:7px}
.map{left:501px;top:785px;width:156px;height:201px;
  background:
    linear-gradient(90deg,rgba(0,0,0,0) 82%,#a9c9e6 88%,#a9c9e6 100%),
    linear-gradient(160deg,#cfe3c0 0%,#ece4cf 25%,#f3d873 45%,#ece4cf 60%,#e6dfcc 80%,#d8e7c6 100%)}
.testimonial{left:76px;top:776px;width:406px;height:120px;background:var(--panel);border:1px solid #ececec}
.testimonial h3{position:absolute;left:0;right:0;top:18px;text-align:center;font-family:"Mulish",sans-serif;font-weight:600;font-size:10.5px;color:var(--teal-text)}
.testimonial p{position:absolute;left:40px;right:25px;top:44px;text-align:center;font-size:6.5px;line-height:12.7px;color:#555}
.quote{font-family:Georgia,serif;font-size:18px;color:#555}
.testimonial .who{position:absolute;left:0;right:0;top:87px;text-align:center;font-family:"Mulish",sans-serif;font-size:10px;color:#555}
.testimonial .who b{font-weight:400;color:var(--teal-text)}
.assoc-title{left:77px;top:908px;font-family:"Mulish",sans-serif;font-weight:600;font-size:10px;color:var(--teal-text)}
.assoc{top:934px;width:98px;height:54px;background:var(--panel);border:1px solid #eee;display:flex;align-items:center;justify-content:center}
.assoc span{width:56px;height:14px;border-radius:7px;background:#d6d6d6}
.footer{left:60px;top:1010px;width:613px;height:190px;background:var(--footer);border-top:3px solid var(--teal)}
.f-head{top:1036px;font-family:"Mulish",sans-serif;font-weight:400;font-size:10px;color:#e4e4e4}
.f-head.social{font-family:"Oswald",sans-serif;font-weight:400;font-size:10.5px}
.f-list{list-style:none;font-size:7.4px;color:var(--footer-text);line-height:14.2px}
.post-thumb{left:207px;width:36px;height:36px}
.post-title{left:250px;font-family:"Mulish",sans-serif;font-size:9px;color:var(--footer-text)}
.post-text{left:250px;width:130px;font-size:6.4px;line-height:12.5px;color:#aaa}
.contact{left:430px;font-size:7.4px;color:var(--footer-text);letter-spacing:.3px}
.social-row{left:602px;display:flex;align-items:center;gap:10px;font-size:7.4px;color:var(--footer-text)}
.social-row i{width:5px;height:5px;background:#bbb}
.copyright{left:76px;top:1178px;font-size:6.4px;color:#aaa}
.legal{left:554px;top:1178px;font-size:6.4px;color:#aaa}
</style>
</head>
<body>
<div class="abs carpet-band" role="img" aria-label="Close-up of green carpet texture"></div>
<div class="abs page"></div>

<header>
  <div class="abs brand"><span class="brand-mark"></span><span class="brand-name">Brightloom Clean</span></div>
  <svg class="abs phone-icon" width="22" height="26" viewBox="0 0 22 26"><path d="M5 2c2-1 3 0 4 3l1 3c0 2-2 2-2 3 1 3 3 6 5 8 1 0 2-2 3-1l3 2c2 1 2 3 0 4-3 2-6 1-9-2C6 18 3 12 3 7c0-2 1-4 2-5z" fill="#d6d6d6"/></svg>
  <div class="abs phone"><b>(555) 014 - 2290</b><span>Call To Action</span></div>
  <nav class="abs nav">
    <a>HOME</a><a>ABOUT</a><a>SERVICES</a><a>BLOG</a><a>EQUIPMENT RENTALS</a><a>TESTIMONIALS</a><a>FREE VIDEOS</a><a>CONTACT US</a>
  </nav>
</header>

<section>
  <div class="abs hero" role="img" aria-label="Technician in jeans vacuuming a beige carpet in front of a white sofa"></div>
  <div class="abs hero-caption">CARPET CLEANING</div>
  <div class="abs hero-arrow" style="left:98px"><svg width="8" height="10"><path d="M6 1L2 5l4 4" stroke="#fff" stroke-width="1.6" fill="none"/></svg></div>
  <div class="abs hero-arrow" style="left:124px"><svg width="8" height="10"><path d="M2 1l4 4-4 4" stroke="#fff" stroke-width="1.6" fill="none"/></svg></div>
</section>

<section>
  <div class="abs tile" style="left:76px">
    <div class="tile-img" role="img" aria-label="Company service van with play button for video testimonials" style="background:linear-gradient(180deg,#8fa7c2 0%,#c9d3dc 30%,#f2f3f3 50%,#e7e9ea 72%,#4a4a4a 88%,#8a8a8a 100%);position:relative">
      <svg style="position:absolute;left:45px;top:20px" width="50" height="50"><circle cx="25" cy="25" r="22" fill="none" stroke="#fff" stroke-width="4" opacity=".85"/><path d="M20 15l14 10-14 10z" fill="#fff" opacity=".85"/></svg>
    </div>
    <div class="tile-label">VIDEO TESTIMONIALS</div>
  </div>
  <div class="abs tile" style="left:223px">
    <div class="tile-img" role="img" aria-label="Gold award trophy on a black base" style="background:radial-gradient(ellipse 14% 40% at 50% 42%,#c9a94a 0,#e2cd86 55%,rgba(250,250,250,0) 100%),linear-gradient(180deg,#fafafa 78%,#2a2a2a 78%,#2a2a2a 90%,#fafafa 90%)"></div>
    <div class="tile-label active">AWARDS</div>
  </div>
  <div class="abs tile" style="left:371px">
    <div class="tile-img" role="img" aria-label="Smiling family lying on a clean carpet" style="background:linear-gradient(135deg,#ece6dc 0%,#d9b89b 30%,#efe9e0 50%,#cfa584 70%,#e6ddd0 100%)"></div>
    <div class="tile-label">Online Reviews <span class="stars">★★★<i>☆☆</i></span></div>
  </div>
  <div class="abs tile" style="left:518px">
    <div class="tile-img" role="img" aria-label="Vacuum cleaning a pink carpet, before and after" style="background:linear-gradient(135deg,#d8bcbf 0%,#b99396 40%,#c8c8cc 55%,#a98285 70%,#c4a2a5 100%)"></div>
    <div class="tile-label">Before &amp; After</div>
  </div>
</section>

<div class="abs divider"></div>

<main>
  <h1 class="abs welcome-title">Welcome To Brightloom Clean</h1>
  <p class="abs body-copy" style="top:647px">Lorem ipsum dolor sit amet, consectetur adipiscing elit, sed do eiusmod tempor incididunt ut labore et dolore magna aliqua. Ut enim ad minim veniam, quis nostrud exercitation ullamco laboris nisi ut aliquip ex ea commodo consequat. Duis aute irure dolor in reprehenderit in voluptate velit esse cillum dolore eu fugiat nulla pariatur. Excepteur sint occaecat cupidatat non proident, sunt in culpa Lorem ipsum dolor sit amet, consectetur adipiscing elit, sed do eiusmod tempor incididunt</p>
  <p class="abs body-copy" style="top:705px">Lorem ipsum dolor sit amet, consectetur adipiscing elit, sed do eiusmod tempor incididunt ut labore et dolore magna aliqua. Ut enim ad minim veniam, quis nostrud exercitation ullamco laboris nisi ut aliquip ex ea commodo consequat. Duis aute irure dolor in reprehenderit in voluptate velit esse cillum dolore eu fugiat nulla pariatur. Excepteur sint occaecat cupidatat non proident, sunt in culpa Lorem ipsum dolor sit amet, consectetur adipiscing elit, sed do eiusmod tempor incididunt</p>

  <div class="abs testimonial">
    <h3>TESTIMONIAL</h3>
    <span class="abs quote" style="left:14px;top:40px">“</span>
    <p>Lorem ipsum dolor sit amet, consectetur adipiscing elit, sed do eiusmod tempor incididunt ut labore et dolore magna aliqua. Ut enim ad minim veniam, quis nostrud exercitation ullamco laboris nisi ut aliquip ex ea commodo consequat. Duis aute irure dolor in reprehenderit in voluptate velit esse cillum</p>
    <div class="who"><b>Marla</b>, Fairhaven</div>
    <span class="abs quote" style="right:14px;top:84px">”</span>
  </div>

  <h2 class="abs assoc-title">ASSOCIATIONS</h2>
  <div class="abs assoc" style="left:76px"><span></span></div>
  <div class="abs assoc" style="left:179px"><span></span></div>
  <div class="abs assoc" style="left:281px"><span></span></div>
  <div class="abs assoc" style="left:384px"><span></span></div>
</main>

<aside>
  <div class="abs sidebar-head">NICHE SERVICES</div>
  <ul class="abs niche-list">
    <li>Resdential</li><li>Commercial</li><li>Carpet Cleaning</li><li>Upholstery Cleaning</li><li>Tile &amp; Grout Cleaning</li>
  </ul>
  <div class="abs map" role="img" aria-label="Street map showing the service area"></div>
</aside>

<footer>
  <div class="abs footer"></div>
  <h4 class="abs f-head" style="left:75px">LIST OF CITIES</h4>
  <ul class="abs f-list" style="left:76px;top:1057px">
    <li>Sed ut perspiciatis</li><li>omnis iste natus</li><li>Lorem ipsum dolor</li><li>consectetur adipiscing</li><li>sed do eiusmod</li><li>dolore magna aliqua</li>
  </ul>

  <h4 class="abs f-head" style="left:206px">LATEST POST</h4>
  <div class="abs post-thumb" style="top:1062px;background:linear-gradient(135deg,#f1ece6,#d7b59a 50%,#a8826a)" role="img" aria-label="Cleaner at work"></div>
  <div class="abs post-title" style="top:1059px">Sed ut perspiciatis unde</div>
  <p class="abs post-text" style="top:1074px">Lorem ipsum dolor sit amet, conseetur adipiscing elit, sed do eiusmod</p>
  <div class="abs post-thumb" style="top:1110px;background:linear-gradient(135deg,#7a4a3a,#c9a58c 55%,#e9e1d6)" role="img" aria-label="Carpet being vacuumed"></div>
  <div class="abs post-title" style="top:1107px">Sed ut perspiciatis unde</div>
  <p class="abs post-text" style="top:1122px">Lorem ipsum dolor sit amet, conseetur adipiscing elit, sed do eiusmod</p>

  <h4 class="abs f-head" style="left:430px">CONTACT US</h4>
  <p class="abs contact" style="top:1055px;line-height:12px">218 Quarry Lane<br>Mesa Verde, NM, 87000<br>United States</p>
  <svg class="abs" style="left:431px;top:1097px" width="10" height="10" viewBox="0 0 22 26"><path d="M5 2c2-1 3 0 4 3l1 3c0 2-2 2-2 3 1 3 3 6 5 8 1 0 2-2 3-1l3 2c2 1 2 3 0 4-3 2-6 1-9-2C6 18 3 12 3 7c0-2 1-4 2-5z" fill="none" stroke="#bbb" stroke-width="2"/></svg>
  <div class="abs contact" style="left:452px;top:1098px">(555) 017-3382</div>
  <svg class="abs" style="left:431px;top:1115px" width="11" height="8"><rect x=".5" y=".5" width="10" height="7" fill="none" stroke="#bbb"/><path d="M.5 .5l5 4 5-4" fill="none" stroke="#bbb"/></svg>
  <div class="abs contact" style="left:452px;top:1113px">info@brightloomcarpets.example</div>

  <h4 class="abs f-head social" style="left:602px">SOCIAL MEDIA</h4>
  <div class="abs social-row" style="top:1060px"><i></i>Friendbook</div>
  <div class="abs social-row" style="top:1077px"><i></i>Chirper</div>
  <div class="abs social-row" style="top:1095px"><i></i>Circles Plus</div>
  <div class="abs social-row" style="top:1112px"><i></i>Tubecast</div>

  <div class="abs copyright">©2013 - 2014 Brightloom Clean, LLC. All Rights Reserved.</div>
  <div class="abs legal">Terms of Service | Privacy Policy</div>
</footer>
</body>
</html>
```